Flyer & Business Card for Lakeside Lens Circle photography courses

I need a flyer design for my company Lakeside Lens Circle - which offers photography classes for all levels in Geneva / Switzerland.

The flyer has to have an attractive visual at the front, and should highlight different types of classes and our teaching philosophy in the back.

Especially the images of Geneva (you can find some on lakesidelenscircle.example and also on my photography website www.morvekimages.example) will help to make people appreciate it's local.

Please check my website to learn more about my company, the logo, brand identity and the overall feeling:
https://www.lakesidelenscircle.example

For the colors, I have used blue in the website and the logo, so it should be somehow compatible.

The final design should communicate fun courses offered by professional photographers that have received consistently 5 star ratings.

Target Market(s)

Geneva / Switzerland

Industry/Entity Type

Business

Contact Information for Business Card

Double sided - front could be a photo (or multiple photos that could be printed as part of one order from pribo.example) and the back should communicate the brand identity.

Colors
0292cd
33a6d7
0555a3

```html
<!DOCTYPE html>
<html lang="en">
<head>
<meta charset="utf-8">
<title>Lakeside Lens Circle – Course Flyer</title>
<link rel="stylesheet" href="https://fonts.googleapis.com/css2?family=Montserrat:wght@400;500;600;700&family=Questrial&family=Pathway+Gothic+One&display=swap">
<style>
  :root {
    --page: #e9e9ea;
    --ink: #050505;
    --card-deep: #0f6cbf;
    --card-light: #27a2de;
    --brand-sky: #33a6d7;
    --brand-blue: #0292cd;
    --text-light: #ffffff;
    --text-dark: #0a1a2a;
    --badge-text: #1f9ad6;
  }
  * { box-sizing: border-box; margin: 0; padding: 0; }
  html, body { width: 1200px; height: 1000px; overflow: hidden; background: var(--page); }
  .canvas { position: relative; width: 1200px; height: 1000px; }

  .flyer {
    position: absolute; left: 272px; top: 30px;
    width: 563px; height: 808px;
    transform: scale(1.163); transform-origin: top left;
    background: var(--ink); overflow: hidden;
    font-family: "Questrial", sans-serif;
  }

  .card {
    position: absolute; width: 173px; height: 166px;
    border-radius: 8px; overflow: hidden; padding: 7px 8px;
  }
  .card--deep { background: var(--card-deep); color: var(--text-light); text-align: center; }
  .card--light { background: var(--card-light); color: var(--text-dark); }
  .col-1 { left: 10px; } .col-2 { left: 193px; } .col-3 { left: 376px; }
  .row-1 { top: 20px; } .row-2 { top: 203px; } .row-3 { top: 388px; }

  .card__heading {
    font-family: "Montserrat", sans-serif; font-weight: 700;
    font-size: 13.5px; line-height: 1.3; letter-spacing: 0.3px;
  }
  .card__text { font-size: 9.6px; line-height: 1.33; }
  .card__title {
    font-family: "Pathway Gothic One", sans-serif; color: var(--text-light);
    font-size: 11.5px; text-transform: uppercase; letter-spacing: 0.2px;
    margin-bottom: 16px;
  }
  .card__icon { display: block; margin: 8px auto 0; }

  .hours-badge {
    position: absolute; right: 2px; bottom: 2px;
    width: 50px; height: 50px; border-radius: 50%;
    background: #fff; box-shadow: 0 0 0 2px var(--card-light);
    color: var(--badge-text); font-size: 9.5px;
    display: flex; align-items: center; justify-content: center;
  }

  .photo { padding: 0; }
  .photo--park { background: linear-gradient(180deg, #7fa35a 0%, #5d8a3e 45%, #9fb38b 75%, #6f8f50 100%); }
  .photo--portrait { background: radial-gradient(circle at 65% 45%, #b48a72 0%, #5a463b 30%, #1c1a19 70%); }

  .team__tag { position: absolute; left: 15px; top: 568px; color: var(--brand-sky); font-size: 10px; }
  .team__intro {
    position: absolute; left: 15px; top: 581px; width: 535px;
    color: var(--text-light); font-size: 9.6px; line-height: 1.35;
  }
  .member { position: absolute; top: 615px; width: 110px; text-align: center; }
  .member__photo { width: 86px; height: 86px; border-radius: 50%; margin: 0 auto; }
  .member__name { margin-top: 11px; font-size: 9.4px; color: var(--brand-sky); white-space: nowrap; }
  .member--1 { left: 48px; } .member--2 { left: 171px; } .member--3 { left: 294px; } .member--4 { left: 415px; }
  .member--1 .member__photo { background: radial-gradient(circle, #8a8f94, #3a3d40); }
  .member--2 .member__photo { background: radial-gradient(circle, #d88a55, #5a2e1a); }
  .member--3 .member__photo { background: radial-gradient(circle, #a3a3a3, #2e2e2e); }
  .member--4 .member__photo { background: radial-gradient(circle, #8c6a4c, #2a1d12); }

  .brand-box {
    position: absolute; left: 15px; top: 728px; width: 130px; height: 53px;
    background: #fff; display: flex; align-items: center; gap: 6px; padding: 0 7px;
  }
  .brand-box__mark { width: 22px; height: 22px; background: var(--ink); flex: none; }
  .brand-box__name {
    font-family: "Montserrat", sans-serif; font-weight: 700; font-size: 10.5px;
    line-height: 1.15; color: var(--ink); text-transform: uppercase;
  }
  .site-url {
    position: absolute; right: 14px; top: 723px;
    font-family: "Montserrat", sans-serif; font-weight: 500;
    font-size: 19px; color: var(--text-light); white-space: nowrap;
  }
  .tagline {
    position: absolute; right: 14px; top: 757px;
    font-family: "Pathway Gothic One", sans-serif;
    font-size: 26px; color: var(--brand-sky); white-space: nowrap;
  }
</style>
</head>
<body>
<div class="canvas">
  <article class="flyer">

    <section class="card card--deep col-1 row-1">
      <h2 class="card__heading">Save you money (!)</h2>
      <p class="card__text">We will focus on improving your photography based on your current equipment. This way you won't fall into the trap that many beginners fall, thinking that they can improve with more expensive equipment.</p>
      <svg class="card__icon" width="18" height="30" viewBox="0 0 18 30" aria-hidden="true">
        <path d="M15 8c-1-3-4-4-6-4-3 0-6 2-6 5s3 4 6 5 6 2 6 5-3 5-6 5-5-1-6-4" fill="none" stroke="#4fb3ea" stroke-width="3" stroke-linecap="round"/>
        <line x1="9" y1="1" x2="9" y2="29" stroke="#4fb3ea" stroke-width="2.5"/>
      </svg>
    </section>

    <div class="card photo photo--park col-2 row-1" role="img" aria-label="Wedding couple on a tree-lined park path holding red heart balloons"></div>

    <section class="card card--light col-3 row-1">
      <h3 class="card__title">Night &amp; Low Light Photography Course</h3>
      <p class="card__text">You love the saturated colours of the "golden hour" and want to experiment with long shutter speeds and HDR photography.</p>
      <span class="hours-badge">3 hours</span>
    </section>

    <section class="card card--deep col-1 row-2">
      <h2 class="card__heading">Money Back<br>Guarantee</h2>
      <p class="card__text">We are confident that you will see absolute improvements in your photography over these two days. However if you feel like you didn't improve by the end of the course, we will reimburse you 100%.</p>
      <svg class="card__icon" width="44" height="40" viewBox="0 0 44 40" aria-hidden="true">
        <path d="M8 14a15 15 0 0 1 26-6" fill="none" stroke="#4fb3ea" stroke-width="3"/>
        <path d="M30 4l5 4-6 3" fill="none" stroke="#4fb3ea" stroke-width="3"/>
        <path d="M36 26a15 15 0 0 1-26 6" fill="none" stroke="#4fb3ea" stroke-width="3"/>
        <path d="M14 36l-5-4 6-3" fill="none" stroke="#4fb3ea" stroke-width="3"/>
        <path d="M26 14c-1-2-2-3-4-3s-4 1-4 3 2 3 4 3 4 1 4 3-2 3-4 3-3-1-4-3" fill="none" stroke="#4fb3ea" stroke-width="2.5"/>
        <line x1="22" y1="8" x2="22" y2="30" stroke="#4fb3ea" stroke-width="2"/>
      </svg>
    </section>

    <section class="card card--light col-2 row-2">
      <h3 class="card__title">PhotoDesk for Photographers Course</h3>
      <p class="card__text">You want to start using the industry leading software for sorting &amp; editing photos and save countless hours in the future.</p>
      <span class="hours-badge">4 hours</span>
    </section>

    <section class="card card--deep col-3 row-2">
      <h2 class="card__heading">Course Notes</h2>
      <p class="card__text">All students will receive comprehensive course notes, personal tips and an invitation to our private Circlebook group where they can post their photos and get constructive critics from the trainers and other students.</p>
      <svg class="card__icon" width="36" height="34" viewBox="0 0 36 34" aria-hidden="true">
        <rect x="4" y="4" width="22" height="28" rx="2" fill="none" stroke="#4fb3ea" stroke-width="2.2"/>
        <path d="M8 1v6M13 1v6M18 1v6M23 1v6" stroke="#4fb3ea" stroke-width="2"/>
        <path d="M31 12l3 3-12 12-4 1 1-4z" fill="none" stroke="#4fb3ea" stroke-width="2"/>
      </svg>
    </section>

    <section class="card card--light col-1 row-3">
      <h3 class="card__title">PixelForge for Photographers Course</h3>
      <p class="card__text">You want to learn how to use PixelForge to improve your photos with our simple proposed tools and guidelines.</p>
      <span class="hours-badge">4 hours</span>
    </section>

    <div class="card photo photo--portrait col-2 row-3" role="img" aria-label="Studio portrait of a smiling man against a dark background"></div>

    <section class="card card--light col-3 row-3">
      <h3 class="card__title">Studio / Portrait Photography Course</h3>
      <p class="card__text">You already know how to use your camera and have a passion to learn about portraiture and studio photography.</p>
      <span class="hours-badge">6 hours</span>
    </section>

    <p class="team__tag">#lakesidelenscircleteam</p>
    <p class="team__intro">Qualified, passionate and with a broad range of professional experience in the industry, our team will make your learning fun, challenging and rewarding!</p>

    <figure class="member member--1">
      <div class="member__photo" role="img" aria-label="Trainer photo holding a camera"></div>
      <figcaption class="member__name">Orhan (Ozzy) Morvek</figcaption>
    </figure>
    <figure class="member member--2">
      <div class="member__photo" role="img" aria-label="Trainer photo holding a camera in warm light"></div>
      <figcaption class="member__name">Elian Tessard</figcaption>
    </figure>
    <figure class="member member--3">
      <div class="member__photo" role="img" aria-label="Black and white trainer portrait"></div>
      <figcaption class="member__name">Julien Sauvain</figcaption>
    </figure>
    <figure class="member member--4">
      <div class="member__photo" role="img" aria-label="Trainer photo with camera"></div>
      <figcaption class="member__name">Luca Ebner</figcaption>
    </figure>

    <div class="brand-box">
      <span class="brand-box__mark"></span>
      <span class="brand-box__name">Lakeside Lens Circle</span>
    </div>
    <p class="site-url">www.lakesidelenscircle.example</p>
    <p class="tagline">Digital Photography Courses for all levels</p>

  </article>
</div>
</body>
</html>
```